Talvex Engineering Business card Design

We need to make business cards for our NDT and inspection company. The company is called Talvex Engineering. We want a professional modern feel business card. We have just completed the remaking of our website and would like to have business cards with the same feel and colours. The final design should communicate professionalism and cutting edge tech.

Target Market(s)

We sell to B2B Business clients. Our customer is an engineer or decision maker in the mechanical engineering / Oil and gas field.

Contact Information for Business Card

Please see the current business cards that we have uploaded to get the details. You can also look at our Website www.talvex-eng.example for more.

Requirements
Must have
• Less is more
Nice to have
• Less is more

```html
<!DOCTYPE html>
<html lang="en">
<head>
<meta charset="utf-8">
<title>Talvex Engineering — Business Card</title>
<link rel="stylesheet" href="https://fonts.googleapis.com/css2?family=Work+Sans:wght@400;500;600;700&display=swap">
<style>
  :root {
    --backdrop: #3b3b3d;
    --card-white: #ffffff;
    --navy: #1d2f6b;
    --red: #b0141b;
    --red-deep: #8e0d13;
    --grey-text: #5b5d63;
    --white: #ffffff;
  }
  * { box-sizing: border-box; margin: 0; padding: 0; }
  html, body {
    width: 1200px; height: 900px; overflow: hidden;
    background: var(--backdrop);
    font-family: "Work Sans", Arial, sans-serif;
  }
  .sheet {
    width: 1200px; height: 900px;
    display: flex; flex-direction: column; align-items: center; justify-content: center;
    gap: 40px;
  }
  .card {
    width: 700px; height: 400px;
    border-radius: 28px;
    position: relative;
    overflow: hidden;
    box-shadow: 0 10px 28px rgba(0,0,0,0.35);
  }

  /* Front */
  .card-front { background: var(--card-white); display: flex; align-items: center; }
  .brand {
    width: 330px; display: flex; flex-direction: column; align-items: center; gap: 18px;
  }
  .brand-mark {
    width: 120px; height: 120px; border-radius: 50%;
    border: 3px solid var(--red);
  }
  .brand-name {
    font-weight: 600; font-size: 24px; color: var(--navy); letter-spacing: 0.5px;
    text-align: center; line-height: 1.2;
  }
  .divider { width: 2px; height: 190px; background: var(--navy); }
  .contact { padding-left: 42px; color: var(--grey-text); }
  .contact-name {
    font-weight: 700; font-size: 30px; color: var(--navy); letter-spacing: 1px; text-transform: uppercase;
  }
  .contact-title { font-size: 19px; margin: 2px 0 18px; }
  .contact-address { font-size: 19px; line-height: 1.3; margin-bottom: 8px; }
  .contact-line { display: flex; align-items: center; gap: 10px; font-size: 19px; line-height: 1.4; }
  .contact-line svg { width: 14px; height: 14px; flex: none; fill: var(--navy); }

  /* Back */
  .card-back {
    background: linear-gradient(135deg, var(--red) 0%, var(--red-deep) 100%);
    color: var(--white);
  }
  .service-list { position: absolute; list-style: none; font-size: 17px; font-weight: 500; line-height: 1.5; }
  .service-list li { display: flex; align-items: center; gap: 12px; }
  .service-list li::before {
    content: ""; width: 10px; height: 10px; border-radius: 50%; background: var(--white); flex: none;
  }
  .services-primary { left: 48px; top: 46px; }
  .services-secondary { left: 360px; top: 200px; }
</style>
</head>
<body>
<main class="sheet">
  <section class="card card-front" aria-label="Business card front">
    <div class="brand">
      <div class="brand-mark"></div>
      <div class="brand-name">Talvex Engineering</div>
    </div>
    <div class="divider"></div>
    <div class="contact">
      <h1 class="contact-name">Adrian Kessler</h1>
      <p class="contact-title">Director</p>
      <p class="contact-address">2215 Harbor<br>Street Lakeview, 40217</p>
      <p class="contact-line">
        <svg viewBox="0 0 16 16" aria-hidden="true"><path d="M3.6 1.2l2.2 2.6-1.3 1.8c.9 2 2.4 3.5 4.4 4.4l1.8-1.3 2.6 2.2-1.4 2.6C6.6 13.3 2.7 9.4 1 3.1z"/></svg>
        +330 5198-2043
      </p>
      <p class="contact-line">
        <svg viewBox="0 0 16 16" aria-hidden="true"><path d="M1 3h14v10H1zm1.5 1.5v.4L8 8.8l5.5-3.9v-.4zm0 2.2v4.8h11V6.7L8 10.6z"/></svg>
        info@talvex-eng.example
      </p>
      <p class="contact-line">
        <svg viewBox="0 0 16 16" aria-hidden="true"><path d="M8 1a7 7 0 100 14A7 7 0 008 1zm0 1.5c.8 0 1.8 1.6 2.1 4.4H5.9C6.2 4.1 7.2 2.5 8 2.5zM2.6 8.4h2.2c.1 1.9.5 3.5 1.1 4.6A5.5 5.5 0 012.6 8.4zm0-1.5A5.5 5.5 0 015.9 3c-.6 1.1-1 2.5-1.1 3.9zM8 13.5c-.8 0-1.8-1.5-2.1-5.1h4.2c-.3 3.6-1.3 5.1-2.1 5.1zm2.1-.5c.6-1.1 1-2.7 1.1-4.6h2.2a5.5 5.5 0 01-3.3 4.6zm1.1-6.1c-.1-1.4-.5-2.8-1.1-3.9a5.5 5.5 0 013.3 3.9z"/></svg>
        www.talvex-eng.example
      </p>
    </div>
  </section>

  <section class="card card-back" aria-label="Business card back">
    <ul class="service-list services-primary">
      <li>API 653 Tank Inspections</li>
      <li>API 570 Pipeline Inspections</li>
      <li>API 510 Pressure Vessel Inspections</li>
      <li>Welding Inspection</li>
      <li>Electrical Inspection</li>
      <li>OCTG Inspections</li>
    </ul>
    <ul class="service-list services-secondary">
      <li>Liting Equipment Inspections</li>
      <li>Non-Destructive Testing</li>
      <li>UT / PT /MT /RT / VT</li>
      <li>Advanced NDT</li>
      <li>PAUT / MFL / ILI</li>
      <li>Engineering Projects</li>
    </ul>
  </section>
</main>
</body>
</html>
```